Cleaning Company Website Design

I am looking for a website design that has my contact information on each page (Call or Text and my e-mail). It should have the main landing page and than pages for Residential Cleaning (Move In/Move Out, Weekly, and Bi-Weekly Cleaning), Commercial Cleaning (Move In/Move Out, Weekly, and Bi-Weekly Cleaning), New Construction Cleaning (Residential, Commercial, and Industrial), and Apartment Turn cleaning for Property Managers. It should list that we carry insurance as well.

Target Market(s)

Residential and Commercial Customers

Industry/Entity Type

Cleaning

Coding

Coded - Design and coding required

Number of Pages Required

5+ page

Requirements
Must have
• A clean professional looking website

```html
<!DOCTYPE html>
<html lang="en">
<head>
<meta charset="UTF-8">
<title>BrightNest Cleaning</title>
<link href="https://fonts.googleapis.com/css2?family=Bebas+Neue&family=Poppins:ital,wght@0,400;0,500;0,600;0,700;1,400&display=swap" rel="stylesheet">
<style>
:root{
  --teal:#1d97ad;
  --teal-dark:#137a8f;
  --navy:#15507f;
  --blue:#1d6fa8;
  --ink:#111417;
  --text:#4a4f55;
  --pale:#eef7fb;
  --white:#fff;
  --gold:#f2a900;
  --footer:#0f1113;
}
*{box-sizing:border-box;margin:0;padding:0}
html,body{width:1200px;height:4464px;overflow:hidden}
body{font-family:'Poppins',sans-serif;color:var(--text);background:var(--white);position:relative}
.wrap{width:1002px;margin:0 auto;position:relative}
.eyebrow{font-size:14px;letter-spacing:5px;color:var(--navy);text-transform:uppercase;font-weight:500}
.h2{font-family:'Bebas Neue',sans-serif;font-size:56px;color:var(--ink);letter-spacing:1px;line-height:1;font-weight:400}
.h2 em{font-style:normal;color:var(--blue)}
.center{text-align:center}
.btn{display:inline-block;background:var(--teal);color:#fff;font-weight:600;font-size:15px;padding:11px 22px;text-transform:uppercase;letter-spacing:.3px}
.photo{display:block}

/* header */
.site-header{height:75px;display:flex;align-items:center;position:relative;background:#fff;box-shadow:0 2px 6px rgba(0,0,0,.08);z-index:3}
.brand{position:absolute;left:99px;top:20px;display:flex;align-items:center;gap:8px;font-weight:600;font-size:20px;color:var(--teal)}
.brand i{width:26px;height:26px;border-radius:50%;background:var(--teal);display:block}
.nav{position:absolute;left:346px;top:28px;display:flex;gap:36px;font-size:14px;font-weight:500;color:var(--ink)}
.nav .active{color:var(--blue)}
.callbar{position:absolute;right:0;top:0;height:75px;width:330px;background:var(--navy);clip-path:polygon(5% 0,100% 0,100% 100%,11% 100%);display:flex;align-items:center;padding-left:60px;gap:14px;color:#fff}
.callbar .ring{width:40px;height:40px;border:2px solid #fff;border-radius:50%;display:flex;align-items:center;justify-content:center}
.callbar small{display:block;font-size:12px}
.callbar b{font-size:19px;font-weight:700}

/* hero */
.hero{height:625px;position:relative}
.hero .photo{position:absolute;inset:0;background:linear-gradient(100deg,#3b3029 0%,#6a5545 40%,#b9b3ab 75%,#d9d6d1 100%)}
.hero-copy{position:absolute;left:99px;top:170px;color:#fff}
.hero-copy .kicker{font-size:13px;font-weight:500}
.hero-copy h1{font-family:'Bebas Neue',sans-serif;font-size:62px;line-height:.95;font-weight:400;margin:12px 0 20px;letter-spacing:1px}
.hero-copy p{font-size:17px;line-height:1.6;width:380px;margin-bottom:24px}
.enquire{position:absolute;left:768px;top:73px;width:335px;height:478px;background:rgba(40,40,40,.88);padding:18px 26px;color:#fff}
.enquire h3{font-family:'Bebas Neue',sans-serif;font-size:28px;text-align:center;font-weight:400}
.enquire .note{font-size:12.5px;line-height:1.4;margin:6px 0 8px}
.enquire label{display:block;font-size:12.5px;margin:10px 0 6px}
.enquire .field{height:37px;background:#fff;position:relative}
.enquire .field.select:after{content:"";position:absolute;right:12px;top:15px;border:7px solid transparent;border-top-color:#111;border-bottom:0}
.enquire .btn{display:block;width:170px;margin:26px auto 0;text-align:center;font-size:16px;padding:10px 0}

/* how it works */
.process{height:639px;background:var(--pale);padding-top:76px}
.steps{display:flex;gap:31px;margin-top:30px}
.step{width:313px;height:388px;background:#fff;box-shadow:0 2px 8px rgba(0,0,0,.08);text-align:center;position:relative}
.step .photo{height:227px}
.step .icon{position:absolute;left:50%;top:183px;transform:translateX(-50%);width:82px;height:82px;border-radius:50%;background:var(--teal);border:4px solid #fff;display:flex;align-items:center;justify-content:center}
.step h3{font-size:22px;font-weight:500;color:var(--ink);margin-top:56px}
.step p{font-size:13.5px;line-height:1.75;padding:4px 28px 0}

/* about */
.about{height:608px;position:relative}
.about .pic1{position:absolute;left:105px;top:70px;width:402px;height:356px;background:linear-gradient(135deg,#dfe5ea,#3c8fcc 55%,#2a6ea6)}
.about .pic2{position:absolute;left:278px;top:244px;width:318px;height:302px;background:linear-gradient(135deg,#f2f4f6,#b9c5cf 60%,#3e5a82);border:6px solid #fff;border-left-width:2px;border-top-width:2px}
.about-copy{position:absolute;left:648px;top:100px;width:454px}
.about-copy .h2{margin:10px 0 24px}
.about-copy p{font-size:13.5px;line-height:2;text-align:justify;margin-bottom:14px}
.about-copy .btn{margin-top:12px}

/* services */
.services{height:689px;background:linear-gradient(180deg,#e7f1f7,#f2f7fa 50%,#e5eff5);padding-top:80px}
.services .lead{font-size:14px;line-height:2;width:640px;margin:14px auto 0}
.offers{display:flex;gap:31px;margin-top:30px}
.offer{width:313px;position:relative;height:375px}
.offer .photo{height:180px}
.offer .box{position:absolute;left:10px;right:10px;top:175px;background:#fff;box-shadow:0 2px 8px rgba(0,0,0,.08);text-align:center;padding:18px 20px 14px}
.offer h3{font-size:18px;font-weight:600;color:var(--ink)}
.offer p{font-size:13px;line-height:2;margin:8px 0 6px}
.offer a{font-size:15px;font-weight:600;color:var(--navy);border-bottom:2px solid var(--navy)}

/* why */
.why{height:563px;position:relative}
.why-copy{position:absolute;left:99px;top:108px;width:475px}
.why-copy .h2{margin:6px 0 20px}
.why-copy p{font-size:13.5px;line-height:2;text-align:justify}
.perks{display:grid;grid-template-columns:205px 270px;row-gap:18px;margin-top:26px}
.perk{display:flex;align-items:center;gap:12px;font-size:14px;font-weight:500;color:var(--ink)}
.perk i{width:48px;height:48px;border-radius:50%;background:var(--teal);display:block;flex:none;border:3px solid #cde9ef}
.why .accent{position:absolute;left:664px;top:68px;width:436px;height:418px;background:var(--navy)}
.why .photo{position:absolute;left:650px;top:82px;width:436px;height:418px;background:linear-gradient(135deg,#eef1f3,#c9d1d8 50%,#2c4f86 80%,#e6cd2f)}

/* testimonials */
.testimonials{height:515px;background:var(--pale);padding-top:70px;position:relative}
.testimonials .h2{margin-top:6px}
.quotes{display:flex;gap:27px;margin-top:34px}
.quote{width:316px;height:276px;background:#fff;box-shadow:0 2px 8px rgba(0,0,0,.1);padding:24px 24px;position:relative}
.stars{color:var(--gold);font-size:20px;letter-spacing:1px}
.quote p{font-style:italic;font-size:14px;line-height:1.85;margin-top:10px}
.quote b{display:block;margin-top:14px;color:var(--teal);font-weight:500;font-size:14px}
.quote small{font-size:12px}
.quote .mark{position:absolute;right:26px;bottom:26px;font-family:'Bebas Neue',sans-serif;font-size:110px;line-height:.6;color:var(--teal);height:44px}
.arrow{position:absolute;top:298px}

/* cta */
.cta{height:396px;background:linear-gradient(180deg,#2ab0b8,#1b8fa7);color:#fff;text-align:center;padding-top:96px}
.cta h2{font-family:'Bebas Neue',sans-serif;font-size:46px;font-weight:400;letter-spacing:1px}
.cta .rule{width:80px;height:3px;background:#fff;margin:14px auto 22px}
.cta p{font-size:14px}
.cta .outline{display:inline-block;border:2px solid #fff;padding:14px 36px;margin-top:36px;font-size:14px;font-weight:600}

/* footer */
.site-footer{height:354px;background:var(--footer);color:#fff;position:relative}
.f-brand{position:absolute;left:99px;top:104px;width:200px;text-align:center}
.f-brand .name{font-size:26px;font-weight:600;display:flex;align-items:center;gap:8px;justify-content:center}
.f-brand .name i{width:22px;height:22px;border-radius:50%;background:#fff;display:block}
.socials{display:flex;gap:14px;justify-content:center;margin-top:20px}
.socials i{width:32px;height:32px;border-radius:50%;background:#fff;display:block}
.f-col{position:absolute;top:58px}
.f-col h4{font-size:20px;font-weight:600;margin-bottom:18px}
.f-col li{list-style:none;font-size:14px;margin-bottom:19px}
.contact li{display:flex;gap:14px;line-height:1.55}
.contact svg{flex:none;margin-top:3px}
.copyright{position:absolute;left:99px;right:99px;bottom:0;border-top:1px solid #333;text-align:center;font-size:13px;padding:18px 0 22px}
</style>
</head>
<body>

<header class="site-header">
  <div class="brand"><i></i>BRIGHTNEST</div>
  <nav class="nav">
    <span class="active">HOME</span><span>ABOUT US</span><span>SERVICES OFFERED ▾</span><span>CONTACT US</span>
  </nav>
  <div class="callbar">
    <div class="ring"><svg width="18" height="18" viewBox="0 0 24 24" fill="#fff"><path d="M6.6 10.8a15.1 15.1 0 0 0 6.6 6.6l2.2-2.2c.3-.3.7-.4 1-.2 1.1.4 2.3.6 3.6.6.6 0 1 .4 1 1V20c0 .6-.4 1-1 1C10.6 21 3 13.4 3 4c0-.6.4-1 1-1h3.5c.6 0 1 .4 1 1 0 1.3.2 2.5.6 3.6.1.3 0 .7-.2 1z"/></svg></div>
    <div><small>CALL OR TEXT</small><b>(555) 014-2290</b></div>
  </div>
</header>

<section class="hero">
  <div class="photo" role="img" aria-label="Cleaners vacuuming and wiping surfaces in a bright home interior"></div>
  <div class="hero-copy">
    <div class="kicker">#1 CLEANING COMPANY</div>
    <h1>PROFESSIONAL<br>CLEANING SERVICE</h1>
    <p>Quality driven and reliable to take care of all your cleaning needs!!!</p>
    <span class="btn">GET STARTED »</span>
  </div>
  <form class="enquire">
    <h3>ENQUIRE</h3>
    <div class="note">Enter your details and our team will contact you soon</div>
    <label>Name*</label><div class="field"></div>
    <label>Email*</label><div class="field"></div>
    <label>Phone Number*</label><div class="field"></div>
    <label>Services Need*</label><div class="field select"></div>
    <span class="btn">BOOK NOW »</span>
  </form>
</section>

<section class="process">
  <div class="wrap center">
    <div class="eyebrow">Our Process</div>
    <h2 class="h2" style="margin-top:10px">HOW IT <em>WORKS</em></h2>
    <div class="steps">
      <div class="step">
        <div class="photo" role="img" aria-label="Hand holding a phone next to a laptop keyboard" style="background:linear-gradient(135deg,#8a6a4c,#3d3a39 60%,#c8ccd0)"></div>
        <div class="icon"><svg width="40" height="40" viewBox="0 0 40 40" fill="none" stroke="#fff" stroke-width="2"><rect x="6" y="9" width="28" height="24" rx="2"/><path d="M6 15h28M13 5v7M27 5v7"/></svg></div>
        <h3>BOOK ONLINE</h3>
        <p>Select the date and time you'd like your professional to show up.</p>
      </div>
      <div class="step">
        <div class="photo" role="img" aria-label="Cleaner in yellow gloves wiping a window" style="background:linear-gradient(135deg,#c9d3dc,#e9c23a 55%,#2a62a8)"></div>
        <div class="icon"><svg width="40" height="40" viewBox="0 0 40 40" fill="none" stroke="#fff" stroke-width="2"><path d="M8 32h24M12 32V18h16v14M20 8v10"/></svg></div>
        <h3>CLEAN</h3>
        <p>A certified cleaner comes over and cleans your house in Atlanta.</p>
      </div>
      <div class="step">
        <div class="photo" role="img" aria-label="Person relaxing on a sofa beside house plants" style="background:linear-gradient(135deg,#dcdad6,#f3f1ee 50%,#7fa36a)"></div>
        <div class="icon"><svg width="40" height="40" viewBox="0 0 40 40" fill="none" stroke="#fff" stroke-width="2"><path d="M8 28c4-8 20-8 24 0M14 14a6 6 0 1 0 12 0 6 6 0 1 0-12 0"/></svg></div>
        <h3>RELAX</h3>
        <p>Sit back, relax and enjoy your sparkling home!</p>
      </div>
    </div>
  </div>
</section>

<section class="about">
  <div class="photo pic1" role="img" aria-label="Cleaning team in blue aprons joining hands"></div>
  <div class="photo pic2" role="img" aria-label="Office cleaners vacuuming an open workspace"></div>
  <div class="about-copy">
    <div class="eyebrow">About Us</div>
    <h2 class="h2">BRIGHTNEST <em>CLEANING</em></h2>
    <p>Lorem ipsum dolor sit amet, consectetur g elit, sed do eiusmod tempor incididunt ut labogna aliqua. Quis ipsum suspendisse ultricgravida. Risus commodo viverra maecenas accumsan lacus vel facilisis.</p>
    <p>We are a fully licensed and insured cleaning company, so every home, office and job site we clean is covered. Our crews carry general liability insurance for your full peace of mind on every visit.</p>
    <span class="btn">LEARN MORE »</span>
  </div>
</section>

<section class="services">
  <div class="wrap center">
    <div class="eyebrow">Services</div>
    <h2 class="h2" style="margin-top:10px">WHAT WE <em>OFFER</em></h2>
    <p class="lead">Lorem ipsum dolor sit amet, consectetur elit, sed do eiusmod tempor incididunt ut labogna aliqua. Quis ipsum suspendisse ultricgravida.</p>
    <div class="offers">
      <div class="offer">
        <div class="photo" role="img" aria-label="Cleaner wiping a kitchen counter" style="background:linear-gradient(135deg,#e3e6e8,#6e4a33 45%,#2f74b5)"></div>
        <div class="box"><h3>RESIDENTIAL CLEANING</h3><p>Lorem ipsum dolor sit amet,sectetur g elit, sed do eiusmodpor incididunt ut labogna aliqua.</p><a>LEARN MORE »</a></div>
      </div>
      <div class="offer">
        <div class="photo" role="img" aria-label="Cleaners mopping a commercial office floor" style="background:linear-gradient(135deg,#4d5a52,#7d8d80 50%,#e8872a)"></div>
        <div class="box"><h3>COMMERCIAL CLEANING</h3><p>Lorem ipsum dolor sit amet,sectetur g elit, sed do eiusmodpor incididunt ut labogna aliqua.</p><a>LEARN MORE »</a></div>
      </div>
      <div class="offer">
        <div class="photo" role="img" aria-label="Worker sanding walls in a newly built room" style="background:linear-gradient(135deg,#cfc7bb,#efece7 50%,#a69a8a)"></div>
        <div class="box"><h3>NEW CONSTRUCTION</h3><p>Lorem ipsum dolor sit amet,sectetur g elit, sed do eiusmodpor incididunt ut labogna aliqua.</p><a>LEARN MORE »</a></div>
      </div>
    </div>
  </div>
</section>

<section class="why">
  <div class="why-copy">
    <div class="eyebrow">Whys Us</div>
    <h2 class="h2">WHY CHOOSE <em>US</em></h2>
    <p>Our trained, background-checked crews are fully insured, so your property is protected on every visit. We show up on time, follow a detailed checklist, use safe products and keep you updated from booking to the final walkthrough.</p>
    <div class="perks">
      <div class="perk"><i></i>Saves Your Time</div>
      <div class="perk"><i></i>Easy To Get Help</div>
      <div class="perk"><i></i>Reliable Crews</div>
      <div class="perk"><i></i>Seamless Communication</div>
    </div>
  </div>
  <div class="accent"></div>
  <div class="photo" role="img" aria-label="Cleaner mopping a floor with a yellow bucket"></div>
</section>

<section class="testimonials">
  <div class="wrap center">
    <div class="eyebrow">Testimonials</div>
    <h2 class="h2">WHAT THEY <em>SAID</em></h2>
    <div class="quotes" style="text-align:left">
      <div class="quote"><div class="stars">★★★★★</div><p>Lorem ipsum dolor sitetur adipiscing elit, sed do eiusmod ter incididunt ut labore et dolore magna aliqua. Quis ipsum suspendisse ultrices gravida. Risus commodo</p><b>JOHN DOE</b><small>Lorem Ips</small><span class="mark">”</span></div>
      <div class="quote"><div class="stars">★★★★★</div><p>Lorem ipsum dolor sitetur adipiscing elit, sed do eiusmod ter incididunt ut labore et dolore magna aliqua. Quis ipsum suspendisse ultrices gravida. Risus commodo</p><b>JOHN DOE</b><small>Lorem Ips</small><span class="mark">”</span></div>
      <div class="quote"><div class="stars">★★★★★</div><p>Lorem ipsum dolor sitetur adipiscing elit, sed do eiusmod ter incididunt ut labore et dolore magna aliqua. Quis ipsum suspendisse ultrices gravida. Risus commodo</p><b>JOHN DOE</b><small>Lorem Ips</small><span class="mark">”</span></div>
    </div>
  </div>
  <svg class="arrow" style="left:50px" width="22" height="34" viewBox="0 0 22 34"><path d="M18 2L4 17l14 15" fill="none" stroke="#333" stroke-width="2"/></svg>
  <svg class="arrow" style="left:1128px" width="22" height="34" viewBox="0 0 22 34"><path d="M4 2l14 15L4 32" fill="none" stroke="#333" stroke-width="2"/></svg>
</section>

<section class="cta">
  <h2>SCHEDULE YOUR BRIGHTNEST CLEANING TODAY</h2>
  <div class="rule"></div>
  <p>book online instantly and schedule your first cleaning for as early tomorrow</p>
  <span class="outline">BOOK HOME CLEANING NOW</span>
</section>

<footer class="site-footer">
  <div class="f-brand">
    <div class="name"><i></i>BRIGHTNEST</div>
    <div class="socials"><i></i><i></i><i></i><i></i></div>
  </div>
  <div class="f-col" style="left:360px"><h4>QUICK LINKS</h4><ul><li>Home</li><li>About Us</li><li>Services Offered</li><li>Contact Us</li></ul></div>
  <div class="f-col" style="left:560px"><h4>SERVICES</h4><ul><li>Residential Cleaning</li><li>Commercial Cleaning</li><li>New Construction Cleaning</li><li>Apartment Cleaning</li></ul></div>
  <div class="f-col contact" style="left:840px"><h4>CONTACT US</h4><ul>
    <li><svg width="14" height="18" viewBox="0 0 14 18"><path d="M7 0a7 7 0 0 1 7 7c0 5-7 11-7 11S0 12 0 7a7 7 0 0 1 7-7zm0 4a3 3 0 1 0 0 6 3 3 0 0 0 0-6z" fill="#fff"/></svg><span>48 Harbor Lane<br>Fairview, US 00000</span></li>
    <li><svg width="16" height="16" viewBox="0 0 24 24" fill="#fff"><path d="M6.6 10.8a15.1 15.1 0 0 0 6.6 6.6l2.2-2.2c.3-.3.7-.4 1-.2 1.1.4 2.3.6 3.6.6.6 0 1 .4 1 1V20c0 .6-.4 1-1 1C10.6 21 3 13.4 3 4c0-.6.4-1 1-1h3.5c.6 0 1 .4 1 1 0 1.3.2 2.5.6 3.6.1.3 0 .7-.2 1z"/></svg><span>(555) 014-2290</span></li>
    <li><svg width="18" height="14" viewBox="0 0 18 14"><rect x="0" y="0" width="18" height="14" rx="1" fill="#fff"/><path d="M1 1l8 7 8-7" fill="none" stroke="#0f1113" stroke-width="1.5"/></svg><span>hello@brightnestclean.com</span></li>
  </ul></div>
  <div class="copyright">©Copyright 2024 The BrightNest Clean. All Rights Reserved.</div>
</footer>

</body>
</html>
```